GPS Fleet Management web application design

We need an application UI design for a GPS fleet management application.
This is a WEB APPLICATION that will run in a desktop browser and not a mobile app design. Looking for a UI/UX expert with experience building desktop application designs.
UI needs to display map with real time location of fleet vehicles
Elements of the application would include things like reporting, geofencing, vehicle on-map displays, alerts, vehicle tabular listing with status (Online, offline, etc), vehicle detail info display like speed, engine rpm, etc etc.
You can blorvex vehicle tracking and get a sense of different GUIs. It is CRITICAL for the designer to understand fleet management applications to be able to do justice to the experience that we are trying to build and be successful in this project.
Looking for something different from the ordinary layout and with some GUI innovation. Should be simple to use, pleasant to look at with proper use of colors and very intuitive. We need a proper framework and user experience built and then on top of that we can add more panes and functionality as needed.
Some UX ideas include hiding things that are not required and resurfacing them easily on demand, being able to move panes around like a canvas, a comprehensive dashboard style layout on login and proper visualization of real time elements as they change.
Once we get some samples we will help the designer perfect it but we need to get some professional UI/UX person to conceptualize and design the user experience.
Reason: Added more time to be able to provide feedback
Gps

```html
<!DOCTYPE html>
<html lang="en">
<head>
<meta charset="utf-8">
<title>Fleet Management Dashboard</title>
<link rel="stylesheet" href="https://fonts.googleapis.com/css2?family=Roboto:wght@300;400;500;900&display=swap">
<style>
  :root {
    --bar-dark: #130c0c;
    --brand-blue: #4a90e2;
    --accent-yellow: #f5a623;
    --ink: #3a3a3a;
    --ink-soft: #555;
    --muted: #8a8a8a;
    --page: #ffffff;
    --stats-bg: #f4f2f1;
    --trend-bg: #fdf8f6;
    --grid: #efe7e4;
    --revenue: #e3ec8e;
    --fleets: #d9b8ec;
    --line: #d8d8d8;
    --status-active: #4a90e2;
    --status-stopped: #f0253f;
    --map-base: #e6e2da;
    --notify: #f0505a;
  }
  * { box-sizing: border-box; margin: 0; padding: 0; }
  html, body { width: 1200px; height: 800px; overflow: hidden; }
  body { font-family: "Roboto", Arial, sans-serif; background: var(--page); color: var(--ink); position: relative; }

  .topbar { position: absolute; left: 0; top: 0; width: 1200px; height: 66px; background: var(--bar-dark); }
  .brand { position: absolute; left: 0; top: 0; width: 227px; height: 66px; background: var(--brand-blue); color: #fff; font-weight: 900; font-size: 19px; letter-spacing: -0.3px; line-height: 66px; padding-left: 16px; }
  .bell { position: absolute; left: 872px; top: 20px; }
  .user-name { position: absolute; left: 918px; top: 22px; color: #fff; font-size: 18px; }
  .avatar { position: absolute; left: 1062px; top: 14px; width: 38px; height: 38px; border-radius: 50%; background: linear-gradient(135deg, #c9a48a, #6e5a4e); }
  .logout { position: absolute; left: 1130px; top: 25px; color: #bdbdbd; font-size: 13px; }

  .sidenav { position: absolute; left: 0; top: 66px; width: 68px; height: 734px; background: var(--bar-dark); }
  .nav-item { position: absolute; left: 0; width: 68px; height: 46px; display: flex; align-items: center; justify-content: center; }
  .nav-item.active { background: #2b2626; border-left: 5px solid var(--accent-yellow); }

  .page-title { position: absolute; left: 83px; top: 78px; font-size: 28px; font-weight: 500; color: var(--ink); }
  .search { position: absolute; left: 896px; top: 80px; width: 288px; height: 35px; border: 1px solid #bbb; border-radius: 18px; padding-left: 15px; font-size: 15px; color: #666; line-height: 33px; }
  .search svg { position: absolute; right: 10px; top: 8px; }

  .stats { position: absolute; left: 68px; top: 130px; width: 1132px; height: 85px; background: var(--stats-bg); }
  .stat { position: absolute; top: 10px; }
  .stat-label { font-size: 15px; color: var(--ink); }
  .stat-value { font-size: 34px; font-weight: 300; color: var(--ink); margin-top: 2px; }
  .range { position: absolute; left: 774px; top: 24px; width: 341px; height: 34px; border: 1px solid #ccc; border-radius: 17px; background: #fff; display: flex; font-size: 15px; color: #aaa; }
  .range span { flex: 1; text-align: center; line-height: 32px; }
  .range .on { flex: 0 0 78px; background: #6b6b6b; color: #fff; border-radius: 17px; }

  .trend { position: absolute; left: 68px; top: 215px; width: 1132px; height: 297px; background: var(--trend-bg); }
  .panel-title { position: absolute; font-size: 18px; color: var(--ink); }
  .legend { position: absolute; top: 19px; font-size: 13px; color: #999; display: flex; align-items: center; gap: 7px; }
  .legend i { width: 12px; height: 12px; border-radius: 50%; border: 2px solid; display: inline-block; }

  .map { position: absolute; left: 77px; top: 555px; width: 547px; height: 245px; background: linear-gradient(135deg, #e9e3d3, #dcdad6 55%, #e8dfc8); }

  .vehicles { position: absolute; left: 641px; top: 556px; width: 552px; height: 236px; border: 1px solid #ddd; }
  .control { position: absolute; top: 11px; height: 29px; border: 1px solid #ccc; border-radius: 15px; font-size: 13px; color: #555; line-height: 27px; padding-left: 14px; }
  .control svg { position: absolute; right: 10px; top: 10px; }
  .table-head { position: absolute; top: 61px; font-size: 15px; color: var(--ink); }
  .head-rule { position: absolute; left: 8px; top: 49px; width: 532px; border-top: 1px solid var(--line); }
  .row { position: absolute; left: 8px; width: 532px; height: 35px; border-bottom: 1px solid #eee; font-size: 13px; color: var(--muted); }
  .row span { position: absolute; top: 11px; }
  .dot { display: inline-block; width: 10px; height: 10px; border-radius: 50%; margin-right: 7px; vertical-align: -1px; }
</style>
</head>
<body>
  <header class="topbar">
    <div class="brand">FLEET MANAGEMENT</div>
    <svg class="bell" width="26" height="26" viewBox="0 0 26 26" fill="none" stroke="#fff" stroke-width="1.6">
      <path d="M4 20h16M6 20v-7a6 6 0 0 1 12 0v7M10 23h4"/>
      <circle cx="20" cy="3" r="3.5" fill="var(--notify)" stroke="none"/>
    </svg>
    <div class="user-name">Marcus Delaney</div>
    <div class="avatar" role="img" aria-label="User profile photo"></div>
    <div class="logout">Log Out</div>
  </header>

  <nav class="sidenav">
    <div class="nav-item active" style="top:39px">
      <svg width="26" height="18" viewBox="0 0 26 18" fill="none" stroke="#fff" stroke-width="2"><path d="M3 15a10 10 0 0 1 20 0"/><path d="M13 14l5-8"/></svg>
    </div>
    <div class="nav-item" style="top:106px">
      <svg width="20" height="24" viewBox="0 0 20 24" fill="none" stroke="#fff" stroke-width="1.8"><path d="M2 1h11l5 5v17H2z"/><path d="M7 14h6"/></svg>
    </div>
    <div class="nav-item" style="top:175px">
      <svg width="26" height="24" viewBox="0 0 26 24" fill="none" stroke="#fff" stroke-width="1.8"><circle cx="13" cy="8" r="6"/><path d="M2 22c2-6 20-6 22 0z"/></svg>
    </div>
    <div class="nav-item" style="top:245px">
      <svg width="28" height="20" viewBox="0 0 28 20" fill="none" stroke="#fff" stroke-width="1.8"><path d="M2 10l3-7h18l3 7v8H2z"/><path d="M2 10h24M6 14h3M19 14h3"/></svg>
    </div>
    <div class="nav-item" style="top:314px">
      <svg width="26" height="22" viewBox="0 0 26 22" fill="none" stroke="#fff" stroke-width="1.8"><path d="M1 3l8-2 8 2 8-2v18l-8 2-8-2-8 2z"/><path d="M9 1v18M17 3v18"/></svg>
    </div>
    <div class="nav-item" style="top:384px">
      <svg width="26" height="26" viewBox="0 0 26 26" fill="none" stroke="#fff" stroke-width="1.8"><circle cx="13" cy="13" r="4"/><path d="M13 2v4M13 20v4M2 13h4M20 13h4M5 5l3 3M18 18l3 3M5 21l3-3M18 8l3-3"/><circle cx="13" cy="13" r="8"/></svg>
    </div>
  </nav>

  <h1 class="page-title">Dashboard</h1>
  <div class="search">Search
    <svg width="18" height="18" viewBox="0 0 18 18" fill="none" stroke="#999" stroke-width="1.6"><circle cx="7.5" cy="7.5" r="6"/><path d="M12 12l5 5"/></svg>
  </div>

  <section class="stats">
    <div class="stat" style="left:15px"><div class="stat-label">Active Fleet</div><div class="stat-value">39</div></div>
    <div class="stat" style="left:144px"><div class="stat-label">Total Revenue</div><div class="stat-value">$65K</div></div>
    <div class="stat" style="left:292px"><div class="stat-label">Reached Destination</div><div class="stat-value">12</div></div>
    <div class="stat" style="left:485px"><div class="stat-label">Performance</div><div class="stat-value">79%</div></div>
    <div class="range"><span class="on">Daily</span><span>This Week</span><span>This Month</span></div>
  </section>

  <section class="trend">
    <h2 class="panel-title" style="left:12px; top:13px">Trend</h2>
    <div class="legend" style="left:950px"><i style="border-color:var(--revenue)"></i>Revenue</div>
    <div class="legend" style="left:1038px"><i style="border-color:var(--fleets)"></i>Fleets</div>
    <svg width="1132" height="297" viewBox="68 215 1132 297" style="position:absolute;left:0;top:0" font-family="Roboto, Arial, sans-serif" font-size="13" fill="#999">
      <g stroke="var(--grid)" stroke-width="1">
        <line x1="160" y1="284" x2="1165" y2="284"/><line x1="160" y1="322" x2="1165" y2="322"/>
        <line x1="160" y1="360" x2="1165" y2="360"/><line x1="160" y1="398" x2="1165" y2="398"/>
        <line x1="160" y1="436" x2="1165" y2="436"/><line x1="160" y1="474" x2="1165" y2="474"/>
      </g>
      <g text-anchor="middle">
        <text x="97" y="284">50</text><text x="97" y="322">40</text><text x="97" y="360">30</text>
        <text x="97" y="398">20</text><text x="97" y="436">10</text><text x="97" y="474">0</text>
        <text x="216" y="499">Mon 10</text><text x="335" y="499">Tue 11</text><text x="454" y="499">Wed 12</text>
        <text x="572" y="499">Thu 13</text><text x="685" y="499">Fri 14</text><text x="795" y="499">Sat 15</text>
        <text x="910" y="499">Sun 16</text><text x="1020" y="499">Mon 17</text><text x="1147" y="499">Tue 18</text>
      </g>
      <polyline fill="none" stroke="var(--fleets)" stroke-width="2" points="218,465 333,432 448,442 573,356 680,391 791,333 895,376 1024,305 1143,375"/>
      <polyline fill="none" stroke="var(--revenue)" stroke-width="3" points="215,389 329,408 449,384 570,428 680,320 789,286 898,428 1021,334 1142,286"/>
      <g fill="var(--fleets)" stroke="#fff" stroke-width="2">
        <circle cx="218" cy="465" r="7"/><circle cx="333" cy="432" r="7"/><circle cx="448" cy="442" r="7"/>
        <circle cx="573" cy="356" r="7"/><circle cx="680" cy="391" r="7"/><circle cx="791" cy="333" r="7"/>
        <circle cx="895" cy="376" r="7"/><circle cx="1024" cy="305" r="7"/><circle cx="1143" cy="375" r="7"/>
      </g>
      <g fill="var(--revenue)" stroke="#fff" stroke-width="2">
        <circle cx="215" cy="389" r="7"/><circle cx="329" cy="408" r="7"/><circle cx="449" cy="384" r="7"/>
        <circle cx="570" cy="428" r="7"/><circle cx="680" cy="320" r="7"/><circle cx="789" cy="286" r="7"/>
        <circle cx="898" cy="428" r="7"/><circle cx="1021" cy="334" r="7"/><circle cx="1142" cy="286" r="7"/>
      </g>
    </svg>
  </section>

  <h2 class="panel-title" style="left:78px; top:526px">Map</h2>
  <div class="map" role="img" aria-label="Street map showing live vehicle positions"></div>

  <h2 class="panel-title" style="left:634px; top:526px">Vehicle List</h2>
  <section class="vehicles">
    <div class="control" style="left:8px; width:173px">All Vehicles
      <svg width="10" height="6" viewBox="0 0 10 6" fill="none" stroke="#777"><path d="M1 1l4 4 4-4"/></svg></div>
    <div class="control" style="left:203px; width:208px; padding-left:10px">Search Vehicle Id,name</div>
    <div class="control" style="left:434px; width:106px">Filter by
      <svg width="10" height="6" viewBox="0 0 10 6" fill="none" stroke="#777"><path d="M1 1l4 4 4-4"/></svg></div>
    <div class="head-rule"></div>
    <div class="table-head" style="left:10px">Status</div>
    <div class="table-head" style="left:218px">Driver</div>
    <div class="table-head" style="left:417px">Vehicle ID</div>

    <div class="row" style="top:86px"><span style="left:4px"><i class="dot" style="background:var(--status-active)"></i>Active</span><span style="left:210px">Owen T Harlow</span><span style="left:409px">#2457956</span></div>
    <div class="row" style="top:121px"><span style="left:4px"><i class="dot" style="background:var(--status-stopped)"></i>Stopped</span><span style="left:210px">Felix Brandt</span><span style="left:409px">#565445</span></div>
    <div class="row" style="top:156px"><span style="left:4px"><i class="dot" style="background:var(--status-active)"></i>Active</span><span style="left:210px">Jonah Reede</span><span style="left:409px">#2456</span></div>
    <div class="row" style="top:191px"><span style="left:4px"><i class="dot" style="background:var(--status-active)"></i>Active</span><span style="left:210px">Owen T Harlow</span><span style="left:409px">#2457956</span></div>
  </section>
</body>
</html>
```